Bright Path Mortgage team needs a booth

we are a mortgage company called WE FIND HOMES and our staff has caricatures designed in SUPER HERO style
we help people that have been turned down at other lenders get a second chance of buying a home
we want to be welcoming yet professional so that they know we take their needs seriously
our slogan is
We Find Homes
It's What We Do!

Industry/Entity Type

It Company

Font styles to use
Sans Serif

Colors
ec1f27
0355a3
fbed22

Requirements
Must have
• 1- 10 ft wide x 8ft high backdrop
• 2- 3ft wide x 8ft wide vertical banners
• 1 table cover 8 ft wide x 2.5 ft high
Nice to have
• i like modern and clean designs

```html
<!DOCTYPE html>
<html lang="en">
<head>
<meta charset="utf-8">
<title>We Find Homes – Booth Banner</title>
<link rel="stylesheet" href="https://fonts.googleapis.com/css2?family=Anton&family=Roboto:wght@400&display=swap">
<style>
  :root {
    --backdrop: #2b2b2b;
    --banner-light: #ffffff;
    --banner-shade: #dcdcdc;
    --brand-blue: #0d3a8a;
    --slogan-red: #b30000;
  }
  html, body {
    margin: 0;
    padding: 0;
    width: 1200px;
    height: 497px;
    overflow: hidden;
    background: var(--backdrop);
  }
  .canvas {
    position: relative;
    width: 1200px;
    height: 497px;
  }
  .banner {
    position: absolute;
    left: 47px;
    top: 75px;
    width: 1105px;
    height: 344px;
    background: linear-gradient(90deg, var(--banner-light) 0%, var(--banner-light) 45%, var(--banner-shade) 100%);
  }
  .brand-name {
    position: absolute;
    left: 0;
    right: 0;
    top: 62px;
    margin: 0;
    text-align: center;
    font-family: "Roboto", sans-serif;
    font-weight: 400;
    font-size: 60px;
    line-height: 1;
    color: var(--brand-blue);
    letter-spacing: 4px;
  }
  .slogan {
    position: absolute;
    left: 0;
    right: 0;
    top: 196px;
    margin: 0;
    text-align: center;
    font-family: "Anton", sans-serif;
    font-weight: 400;
    font-size: 112px;
    line-height: 1;
    color: var(--slogan-red);
    letter-spacing: 1px;
  }
</style>
</head>
<body>
  <div class="canvas">
    <section class="banner">
      <h1 class="brand-name">WE FIND HOMES</h1>
      <p class="slogan">IT’S WHAT WE DO!</p>
    </section>
  </div>
</body>
</html>
```